Business card design needed

Need a new business card design for a new business in Sydney, Australia called 'Verrowin Australia'. The business deals in consulting for new sales, sales leadership and customer service consultancy. Want the business card to look professional and clean

Industry/Entity Type

Leadership

Contact Information for Business Card

Verrowin Australia
Tobias Wrenley
Managing Director

14 Quarrion Avenue
Marrowdale NSW 2041

0432 517 806
tobias@verrowin.com.au
www.verrowin.com.au

```html
<!DOCTYPE html>
<html lang="en">
<head>
<meta charset="utf-8">
<title>Verrowin Australia – Business Card</title>
<link href="https://fonts.googleapis.com/css2?family=Didact+Gothic&display=swap" rel="stylesheet">
<style>
  :root {
    --page: #ffffff;
    --card-dark: #1c1d1d;
    --card-mid: #3a3b3b;
    --card-back: #343535;
    --green: #8aa63c;
    --green-band: #7e9b38;
    --text-light: #f2f2f2;
    --text-muted: #cfd2cf;
    --divider: #6e716f;
  }
  * { margin: 0; padding: 0; box-sizing: border-box; }
  html, body { width: 1005px; height: 1200px; overflow: hidden; background: var(--page); }
  body { position: relative; font-family: "Didact Gothic", "Century Gothic", sans-serif; }

  .card { position: absolute; border-radius: 40px; overflow: hidden; }

  .card-front {
    left: 30px; top: 24px; width: 945px; height: 545px;
    background: radial-gradient(ellipse 60% 60% at 52% 48%, var(--card-mid) 0%, var(--card-dark) 80%, #111 100%);
    box-shadow: 0 2px 4px rgba(0,0,0,.35);
  }
  .front-wordmark {
    position: absolute; left: 180px; top: 200px;
    font-size: 66px; color: var(--text-light); letter-spacing: -1px; white-space: nowrap;
  }
  .service { position: absolute; font-size: 22px; white-space: nowrap; display: flex; align-items: center; }
  .service::before { content: ""; width: 9px; height: 9px; border-radius: 50%; background: currentColor; margin-right: 9px; }
  .service-sales { left: 180px; top: 300px; color: var(--green); }
  .service-leadership { left: 332px; top: 330px; color: var(--text-light); }
  .service-customer { left: 436px; top: 360px; color: var(--green); }

  .card-back {
    left: 28px; top: 626px; width: 940px; height: 540px;
    background: var(--card-back);
  }
  .back-wordmark {
    position: absolute; left: 0; right: 0; top: 148px; text-align: center;
    font-size: 56px; color: var(--text-light); letter-spacing: -1px;
  }
  .person { position: absolute; left: 186px; top: 300px; text-align: center; }
  .person-name { font-size: 36px; color: var(--green); letter-spacing: .5px; }
  .person-role { font-size: 22px; color: var(--text-muted); margin-top: 4px; }

  .divider { position: absolute; left: 482px; top: 274px; width: 3px; height: 180px; background: var(--divider); }

  .contact-band {
    position: absolute; left: 492px; top: 280px; width: 448px; height: 134px;
    background: var(--green-band); padding: 18px 0 0 40px;
  }
  .contact-line { display: flex; align-items: center; height: 36px; font-size: 20px; color: var(--text-light); }
  .contact-line svg { width: 22px; height: 22px; margin-right: 18px; fill: var(--text-light); flex: none; }
  .website { position: absolute; left: 492px; top: 428px; font-size: 20px; color: var(--green); }
</style>
</head>
<body>
  <section class="card card-front">
    <div class="front-wordmark">Verrowin Australia</div>
    <div class="service service-sales">consulting for new sales</div>
    <div class="service service-leadership">sales leadership</div>
    <div class="service service-customer">customer service consultancy</div>
  </section>

  <section class="card card-back">
    <div class="back-wordmark">Verrowin Australia</div>
    <div class="person">
      <div class="person-name">Tobias Wrenley</div>
      <div class="person-role">Managing Director</div>
    </div>
    <div class="divider"></div>
    <div class="contact-band">
      <div class="contact-line">
        <svg viewBox="0 0 24 24" aria-hidden="true"><path d="M7 2c1 0 1.6.5 2 1.5l1.2 3c.3.9 0 1.6-.7 2.2l-1.2 1c.9 2 2.4 3.6 4.3 4.6l1-1.2c.6-.7 1.4-1 2.2-.7l3 1.3c1 .4 1.4 1 1.4 2L20 19c-.3 1.8-1.8 3-3.6 2.8C9 21 3 15 2.2 7.6 2 5.8 3.2 4.3 5 4z"/></svg>
        0432 517 806
      </div>
      <div class="contact-line">
        <svg viewBox="0 0 24 24" aria-hidden="true"><path d="M2 5h20v14H2zm2 2v.4l8 5.4 8-5.4V7zm0 2.8V17h16V9.8l-8 5.4z"/></svg>
        tobias@verrowin.com.au
      </div>
      <div class="contact-line">
        <svg viewBox="0 0 24 24" aria-hidden="true"><path d="M12 3l10 9h-3v9h-5v-6h-4v6H5v-9H2z"/></svg>
        14 Quarrion Avenue Marrowdale NSW 2041
      </div>
    </div>
    <div class="website">www.verrowin.com.au</div>
  </section>
</body>
</html>
```